deceased estate clean ups brochures

we would like a brochure to reresent our business we already have new web site and want to do DL A4 brochure to give out to promote our business we already have logo www.brightvale.com.au is where you can get all info needed

Target Market(s)

families with loved ones that have past away
people done sizing or needing to decluter

Colors
cadf82
33b8a4
886aae
33a6d7

```html
<!DOCTYPE html>
<html lang="en">
<head>
<meta charset="utf-8">
<title>Brightvale – Deceased Estate Cleanups DL Flyer</title>
<link rel="stylesheet" href="https://fonts.googleapis.com/css2?family=Caprasimo&family=Roboto:wght@400;500;700&display=swap">
<style>
  :root {
    --page-bg: #e4e4e4;
    --paper: #ffffff;
    --green: #5aa84a;
    --green-deep: #3e8a34;
    --green-light: #8cc63f;
    --green-pale: #b9dc7c;
    --ink: #1a1a1a;
    --white: #ffffff;
  }
  * { box-sizing: border-box; margin: 0; padding: 0; }
  html, body { width: 1200px; height: 1000px; overflow: hidden; }
  body {
    background: var(--page-bg);
    font-family: "Roboto", Arial, sans-serif;
    position: relative;
  }
  .flyer {
    position: absolute;
    left: 365px; top: 0;
    width: 470px; height: 1000px;
    background: var(--paper);
    overflow: hidden;
  }
  .flyer__wave { position: absolute; left: 0; top: 0; width: 470px; height: 1000px; }

  .brand {
    position: absolute; top: 55px; left: 0; width: 100%;
    display: flex; justify-content: center; align-items: center; gap: 14px;
  }
  .brand__dot { width: 34px; height: 34px; border-radius: 50%; background: var(--green); }
  .brand__name {
    font-family: "Roboto", Arial, sans-serif; font-weight: 700;
    font-size: 44px; letter-spacing: 2px; color: var(--ink);
  }

  .headline {
    position: absolute; top: 132px; left: 0; width: 100%;
    text-align: center;
    font-family: "Caprasimo", "Cooper Black", serif;
    color: var(--white);
    line-height: 1.08;
    text-shadow:
      -2px -2px 0 var(--green-light), 2px -2px 0 var(--green-light),
      -2px 2px 0 var(--green-light), 2px 2px 0 var(--green-light),
      3px 4px 0 var(--green-deep), 4px 6px 0 var(--green-deep), 5px 7px 6px rgba(0,0,0,.25);
  }
  .headline__line1 { display: block; font-size: 45px; transform: rotate(3deg); }
  .headline__line2 { display: block; font-size: 45px; transform: rotate(2deg); }

  .intro {
    position: absolute; top: 258px; left: 50px; width: 370px;
    text-align: center; color: var(--white);
    font-size: 17px; line-height: 1.3;
  }

  .section-title {
    position: absolute; top: 334px; left: 0; width: 100%;
    text-align: center;
    font-family: "Caprasimo", "Cooper Black", serif;
    font-size: 40px; color: var(--white);
    text-shadow:
      -2px -2px 0 var(--green-light), 2px -2px 0 var(--green-light),
      -2px 2px 0 var(--green-light), 2px 2px 0 var(--green-light),
      3px 4px 0 var(--green-deep), 4px 6px 0 var(--green-deep);
  }

  .services {
    position: absolute; top: 404px; left: 60px; width: 362px;
    display: grid; grid-template-columns: 160px 160px; column-gap: 42px; row-gap: 0;
    list-style: none;
  }
  .service { height: 150px; display: flex; flex-direction: column; align-items: center; }
  .service:nth-child(n+3) { height: 140px; }
  .service__photo {
    width: 160px; height: 82px; border-radius: 10px;
    border: 3px solid var(--white);
    box-shadow: 5px 5px 0 var(--green-pale);
  }
  .service__label {
    margin-top: 14px; text-align: center; color: var(--white);
    font-weight: 500; font-size: 15.5px; line-height: 1.18; text-transform: uppercase;
  }
  .photo--care { background: linear-gradient(135deg, #f4efe8, #c9b9a6); }
  .photo--repairs { background: linear-gradient(180deg, #9db0c2, #d6d0c4 55%, #8c7e6c); }
  .photo--cleaning { background: linear-gradient(135deg, #eef0ee, #c5cbd0 60%, #6e7c8a); }
  .photo--estate { background: linear-gradient(180deg, #6fa4d8, #b58d6c 45%, #5c7a43); }
  .photo--moving { background: linear-gradient(135deg, #f1ede6, #b89a7a 60%, #7a6a5c); }
  .photo--garden { background: linear-gradient(135deg, #6aa83f, #2f6a24 60%, #9ac454); }

  .contact {
    position: absolute; top: 906px; left: 0; width: 100%;
    list-style: none; text-align: center;
    color: var(--green-deep); font-weight: 700; font-size: 18px; line-height: 24px;
  }
  .contact__item { display: flex; justify-content: center; align-items: center; gap: 14px; }
  .contact__icon { width: 14px; height: 14px; fill: var(--green-deep); }
</style>
</head>
<body>
<main class="flyer">
  <svg class="flyer__wave" viewBox="0 0 470 1000" aria-hidden="true">
    <path d="M0 262 C120 170 330 150 470 172 L470 880 C330 905 140 905 0 850 Z" fill="var(--green-pale)"/>
    <path d="M0 272 C120 185 330 165 470 185 L470 872 C330 897 140 897 0 842 Z" fill="var(--green)"/>
  </svg>

  <header class="brand">
    <span class="brand__dot"></span>
    <span class="brand__name">BRIGHTVALE</span>
  </header>

  <h1 class="headline">
    <span class="headline__line1">Deceased Estate</span>
    <span class="headline__line2">Cleanups</span>
  </h1>

  <p class="intro">At Brightvale our goal is to ease your worries and help you with your journey in preparing your house for rental or resale.</p>

  <h2 class="section-title">Services Offered</h2>

  <ul class="services">
    <li class="service">
      <div class="service__photo photo--care" role="img" aria-label="Carer supporting an elderly resident"></div>
      <span class="service__label">Senior / Aged<br>Care Relocations<br>and Down Sizing</span>
    </li>
    <li class="service">
      <div class="service__photo photo--repairs" role="img" aria-label="House exterior with ladders during repairs"></div>
      <span class="service__label">Cosmetic Repairs<br>and House<br>Maintenance</span>
    </li>
    <li class="service">
      <div class="service__photo photo--cleaning" role="img" aria-label="Cleaners wiping and mopping a bright room"></div>
      <span class="service__label">Cleaning<br>Service</span>
    </li>
    <li class="service">
      <div class="service__photo photo--estate" role="img" aria-label="Brick family home with tiled roof"></div>
      <span class="service__label">Deceased<br>Estates</span>
    </li>
    <li class="service">
      <div class="service__photo photo--moving" role="img" aria-label="Couple moving furniture and boxes"></div>
      <span class="service__label">Preparation for<br>Rental or Sale</span>
    </li>
    <li class="service">
      <div class="service__photo photo--garden" role="img" aria-label="Gloved hand pulling weeds in a garden bed"></div>
      <span class="service__label">Garden<br>Makeovers</span>
    </li>
  </ul>

  <ul class="contact">
    <li class="contact__item">
      <svg class="contact__icon" viewBox="0 0 14 14" aria-hidden="true"><path d="M2 0 L12 8 L7.5 8.5 L10 13 L8 14 L5.5 9.5 L2 12 Z"/></svg>
      <span>www.brightvalemelbourne.com.au</span>
    </li>
    <li class="contact__item">
      <svg class="contact__icon" viewBox="0 0 14 14" aria-hidden="true"><path d="M0 3 H14 V12 H0 Z" opacity=".9"/><path d="M0 3 L7 8 L14 3" fill="none" stroke="#fff" stroke-width="1.3"/></svg>
      <span>info@brightvalemelbourne.com.au</span>
    </li>
    <li class="contact__item">
      <svg class="contact__icon" viewBox="0 0 14 14" aria-hidden="true"><path d="M3 0.5 L5.5 3.5 L4 5.5 C5 7.5 6.5 9 8.5 10 L10.5 8.5 L13.5 11 L11.5 13.5 C6 13 1 8 0.5 2.5 Z"/></svg>
      <span>0400 123 456</span>
    </li>
  </ul>
</main>
</body>
</html>
```